Business Card Design

We need a business card designed for our new company. Prefer a black card with white logo & writing.

Contact Information for Business Card

Dov Telling, address: 3-4817 Fernwick Avenue, Abbotsford, BC, V8K 2P9, Office Phone: 604-913-2760, Cell: 604-271-4053, Email: dov@qlresinhaus.ca

Colors

Designer to choose only greyscale colors for use in the design.

```html
<!DOCTYPE html>
<html lang="en">
<head>
<meta charset="utf-8">
<title>QL Resin Haus — Business Card</title>
<link href="https://fonts.googleapis.com/css2?family=Montserrat:wght@400;700;800&family=Lato:wght@400&display=swap" rel="stylesheet">
<style>
  :root {
    --backdrop: #2e2e2e;
    --card: #1f1f1f;
    --ink: #ffffff;
    --ink-soft: #d9d9d9;
    --rule: #e6e6e6;
  }
  * { box-sizing: border-box; margin: 0; padding: 0; }
  html, body { width: 1200px; height: 895px; overflow: hidden; }
  body {
    background: var(--backdrop);
    position: relative;
    font-family: "Lato", sans-serif;
    color: var(--ink);
  }
  .card {
    position: absolute;
    width: 620px;
    height: 354px;
    background: var(--card);
    border-radius: 22px;
    box-shadow: 0 14px 30px rgba(0,0,0,0.45);
  }
  .card--front { left: 110px; top: 60px; }
  .card--back  { left: 470px; top: 480px; }

  .brand {
    position: absolute;
    display: flex;
    align-items: center;
    gap: 12px;
    font-family: "Montserrat", sans-serif;
    font-weight: 800;
    color: var(--ink);
    text-transform: uppercase;
    letter-spacing: 1px;
    white-space: nowrap;
  }
  .brand__mark {
    border: 3px solid var(--ink);
    flex: none;
  }
  .card--front .brand {
    left: 50%; top: 50%;
    transform: translate(-50%, -50%);
    font-size: 44px;
  }
  .card--front .brand__mark { width: 40px; height: 40px; }
  .card--back .brand {
    right: 36px; top: 62px;
    font-size: 28px;
  }
  .card--back .brand__mark { width: 26px; height: 26px; border-width: 2px; }

  .holder {
    position: absolute;
    left: 42px; top: 160px;
  }
  .holder__name {
    font-family: "Montserrat", sans-serif;
    font-weight: 700;
    font-size: 24px;
    line-height: 1.1;
  }
  .holder__title {
    font-family: "Montserrat", sans-serif;
    font-weight: 400;
    font-size: 17px;
    color: var(--ink-soft);
    margin-top: 4px;
  }
  .divider {
    position: absolute;
    left: 42px; right: 40px; top: 218px;
    height: 1.5px;
    background: var(--rule);
  }
  .contacts {
    position: absolute;
    left: 42px; top: 234px;
    list-style: none;
    font-size: 17px;
  }
  .contacts__item {
    display: flex;
    align-items: center;
    gap: 12px;
    height: 30px;
  }
  .contacts__icon { width: 18px; height: 18px; flex: none; }
  .address {
    position: absolute;
    right: 40px; top: 236px;
    text-align: right;
    font-size: 17px;
    line-height: 30px;
  }
</style>
</head>
<body>

  <section class="card card--front" aria-label="Card front">
    <div class="brand">
      <span class="brand__mark"></span>
      <span class="brand__name">QL Resin Haus</span>
    </div>
  </section>

  <section class="card card--back" aria-label="Card back">
    <div class="brand">
      <span class="brand__mark"></span>
      <span class="brand__name">QL Resin Haus</span>
    </div>

    <div class="holder">
      <p class="holder__name">Dov Telling</p>
      <p class="holder__title">President</p>
    </div>

    <div class="divider"></div>

    <ul class="contacts">
      <li class="contacts__item">
        <svg class="contacts__icon" viewBox="0 0 24 24" aria-hidden="true">
          <path fill="#fff" d="M6.6 10.8a15.1 15.1 0 0 0 6.6 6.6l2.2-2.2a1 1 0 0 1 1-.25 11.4 11.4 0 0 0 3.6.57 1 1 0 0 1 1 1V20a1 1 0 0 1-1 1A17 17 0 0 1 3 4a1 1 0 0 1 1-1h3.5a1 1 0 0 1 1 1c0 1.25.2 2.45.57 3.57a1 1 0 0 1-.25 1z"/>
        </svg>
        <span>604-913-2760</span>
      </li>
      <li class="contacts__item">
        <svg class="contacts__icon" viewBox="0 0 24 24" aria-hidden="true">
          <rect x="6" y="2" width="12" height="20" rx="2" fill="none" stroke="#fff" stroke-width="1.8"/>
          <circle cx="12" cy="18.5" r="1" fill="#fff"/>
        </svg>
        <span>604-271-4053</span>
      </li>
      <li class="contacts__item">
        <svg class="contacts__icon" viewBox="0 0 24 24" aria-hidden="true">
          <rect x="2" y="5" width="20" height="14" fill="none" stroke="#fff" stroke-width="1.8"/>
          <path d="M2 5l10 8 10-8" fill="none" stroke="#fff" stroke-width="1.8"/>
        </svg>
        <span>dov@qlresinhaus.ca</span>
      </li>
    </ul>

    <address class="address" style="font-style:normal">
      3-4817 Fernwick Avenue,<br>
      Abbotsford, BC, V8K 2P9,
    </address>
  </section>

</body>
</html>
```